・「暑中見舞い」というコンセプトと「DM」という目的に沿ったデザインを提案してください。
・文字要素が多いですが、シンプルに整理して読みやすくスタイリッシュなデザインをお願いしたいです。
・用意したテキスト(パワーポイントとPDF)だけだとカタイので、デザインのどこかに工夫やアイデアを1つ入れてほしいです。また、「こうしたほうがいい」というご提案であれば、テキスト細部の変更もOKです。
・使う用紙は、官製はがき(すずかぜ~ん)です。フチ四隅が印刷できない、切手欄やくじ部分が印刷できないなどの制限があります。添付の印刷所指定テンプレを使用したほうが間違いがないと思います。
表面:宛名書き、暑中見舞いご挨拶 裏面:キャンペーン告知、自社紹介
(添付資料参照)
• イラストレーター形式 (.ai)
• フォトショップ形式 (.psd)
印刷所対応フォーマットで納品してください。
後日別案件の相談も可能性あります。
資料のアップロードがうまくいってなかったようなので
再度アップします。
ロゴデータくらい必要でしたね。。。大変失礼しました。
イラレの古いデータアップしますので、使う場合はロゴはこちらから抜いてください。
もちろんご提案の段階ではアタリで構いません。

>各位
すずかぜーんの配送ルール(特に宛名面のほう)がありますので、採用後に調整お願いすると思います。大変お手数とは思いますが、ご対応お願いいたします。

理屈でなく、面白いなと感じました。DMなので、受け取る人が「おっ!」なるものがいいかなと思いました。

数多くのご提案、どうもありがとうございました。
狭いスペースに情報量が多く難しいと思いましたが、個性的なアイデアがいくつか見られてとてもよかったです。高い技術をお持ちの方もかなりいらっしゃったので、今後もお仕事をお願いしてみたいと考えています。
引き続きどうぞよろしくお願いします。

```html
<!DOCTYPE html>
<html lang="ja">
<head>
<meta charset="utf-8">
<title>暑中お見舞い DM</title>
<link rel="stylesheet" href="https://fonts.googleapis.com/css2?family=Noto+Sans+JP:wght@400;500;700;900&display=swap">
<style>
  :root {
    --paper: #ffffff;
    --ink: #1c1c1c;
    --accent-blue: #1f6fc0;
    --accent-orange: #e8731e;
    --book-top: #f3efe2;
    --book-mid: #7fb24a;
    --book-low: #d9c9a3;
    --rule: #e2e2e2;
  }
  * { margin: 0; padding: 0; box-sizing: border-box; }
  html, body {
    width: 824px; height: 1200px; overflow: hidden;
    background: var(--paper);
  }
  .postcard {
    position: relative;
    width: 824px; height: 1200px;
    background: var(--paper);
    color: var(--ink);
    font-family: "Noto Sans JP", sans-serif;
  }
  .campaign-label {
    position: absolute; left: 126px; top: 318px;
    font-size: 30px; font-weight: 700; line-height: 1;
    color: var(--accent-orange);
  }
  .campaign-item {
    position: absolute; left: 165px; top: 371px;
    width: 181px; height: 296px;
    background: linear-gradient(180deg, var(--book-top) 0%, var(--book-top) 30%, var(--book-mid) 30%, var(--book-mid) 62%, var(--book-low) 62%, var(--book-low) 100%);
    box-shadow: 2px 3px 6px rgba(0,0,0,0.25);
  }
  .addressee {
    position: absolute; left: 432px; top: 378px;
    width: 300px;
    font-size: 58px; font-weight: 500;
    line-height: 1.45;
    text-align: center;
  }
  .divider {
    position: absolute; left: 110px; top: 676px;
    width: 680px; height: 1px;
    background: var(--rule);
  }
  .greeting {
    position: absolute; left: 110px; top: 680px;
    font-size: 52px; font-weight: 700; line-height: 1.1;
    color: var(--accent-blue);
    white-space: nowrap;
  }
  .message-line {
    position: absolute; left: 151px;
    font-size: 25px; font-weight: 400;
    line-height: 1.2; white-space: nowrap;
  }
  .company {
    font-size: 30px; font-weight: 700;
    color: var(--accent-blue);
  }
  .campaign-name {
    font-size: 34px; font-weight: 700;
    color: var(--accent-blue);
  }
  .season-date {
    position: absolute; right: 30px; top: 1103px;
    font-size: 19px; line-height: 1.2;
  }
</style>
</head>
<body>
  <main class="postcard">
    <p class="campaign-label">キャンペーン品！</p>
    <div class="campaign-item" role="img" aria-label="キャンペーン品のランチガイドブックの表紙写真"></div>

    <h2 class="addressee">福岡市の<br>みなさまへ</h2>

    <div class="divider"></div>

    <h1 class="greeting">暑中お見舞い申し上げます</h1>

    <p class="message-line" style="top:762px">連日暑い日が続きますがいかがお過ごしでしょうか？</p>
    <p class="message-line" style="top:795px">平素は格別のお引き立てをいただき</p>
    <p class="message-line" style="top:828px">誠にありがとうございます。</p>
    <p class="message-line" style="top:878px">ただいま<span class="company">制作会社ソラノワ</span>では</p>
    <p class="message-line" style="top:920px">福岡の方ともっとお知り合いになるべく、</p>
    <p class="message-line" style="top:950px"><span class="campaign-name">「はじめまして夏キャンペーン」</span></p>
    <p class="message-line" style="top:1001px">を実施中です！</p>
    <p class="message-line" style="top:1034px">御社のお悩み解決のため、ぜひお問い合わせください。</p>
    <p class="message-line" style="top:1067px">炎暑のみぎり、くれぐれもご自愛ください。</p>

    <p class="season-date">平成28年　盛夏</p>
  </main>
</body>
</html>
```